High end wine label at Austrian Winery

We are a traditional winery in Austria in region Burgenland. We are looking for a relaunch of our current wine label for our [solstice] series. It's a high end wine series at an upper price range. At the moment we have just two kinds of the label, one white one for the white wines and one black one for the red wines. This is a series of wine, white, red, sweet, sparkling and a top wine categories. So we need the same label, but in 4 different ways to distinguish the wines plus the sparkling. Maybe in color, patterns, ... or something else. The label should be very simple, including our new logo. It's also possible to make one label but we can splitting two parts of the label. The size of the label does not matter, need not be the same as now. It's a bit higher than a normal bottle. Additionally we need a back label with wine description and the wine dates on it.

Target Market(s)

private consumers and restaurants, no retailers

Colors

Designer to choose colors to be used in the design.

Requirements
Must have
• simple label with 4 different categories (red, white, sweet, top) plus Frizzante label, new logo integrated, high end label. Just logo, grape variety and [solstice] as text on the front label as text
Nice to have
• It's just good, if there'sa possibility to have different colors of each grape variety (about 10 different), but all the same style. top Wines should have an extraordinary design, but familiar with the others
Should not have
• no cheap look

```html
<!DOCTYPE html>
<html lang="en">
<head>
<meta charset="utf-8">
<title>HALDEN [solstice] wine labels</title>
<link href="https://fonts.googleapis.com/css2?family=Cinzel:wght@400&family=Montserrat:wght@700&family=Allura&display=swap" rel="stylesheet">
<style>
  :root {
    --page: #ffffff;
    --cream: #f3efd3;
    --ink: #2a2622;
    --night: #121212;
    --gold: #b8955a;
    --silver: #cfcac0;
    --purple: #6a4a7f;
    --purple-soft: #9c84a8;
    --green: #8dc153;
    --green-soft: #c6dea4;
    --red: #e5443a;
    --red-soft: #f2a393;
    --yellow: #ddc46a;
    --yellow-soft: #ebdfa6;
  }
  * { margin: 0; padding: 0; box-sizing: border-box; }
  html, body { width: 1200px; height: 944px; overflow: hidden; background: var(--page); }
  .label-row {
    width: 1200px; height: 944px;
    display: flex; justify-content: center; align-items: center; gap: 24px;
  }
  .label {
    width: 206px; height: 200px;
    background: var(--cream);
    display: flex; flex-direction: column; align-items: center;
    box-shadow: 0 2px 10px rgba(0,0,0,0.08);
  }
  .brand-mark {
    width: 58px; height: 58px; margin-top: 22px;
    border-radius: 50%; border: 2px solid var(--ink);
  }
  .brand-name {
    margin-top: 9px;
    font-family: "Montserrat", sans-serif; font-weight: 700;
    font-size: 13px; letter-spacing: 1.5px; color: var(--ink);
  }
  .brand-tagline {
    margin-top: 1px;
    font-family: "Montserrat", sans-serif; font-weight: 700;
    font-size: 5px; letter-spacing: 1.2px; color: var(--ink);
  }
  .series-band {
    margin-top: auto; width: 100%; height: 17px;
    display: flex; align-items: center; justify-content: center;
    font-family: "Montserrat", sans-serif; font-weight: 700;
    font-size: 5.5px; letter-spacing: 1px; color: var(--ink);
  }
  .variety-band {
    width: 100%; height: 38px;
    display: flex; align-items: center; justify-content: center;
    font-family: "Cinzel", serif; font-size: 13px; letter-spacing: 0.5px;
    color: #fbf8ea;
  }
  .label--blaufrankisch .series-band { background: var(--purple-soft); }
  .label--blaufrankisch .variety-band { background: var(--purple); }
  .label--pinot .series-band { background: var(--green-soft); }
  .label--pinot .variety-band { background: var(--green); }
  .label--cabernet .series-band { background: var(--red-soft); }
  .label--cabernet .variety-band { background: var(--red); }
  .label--veltliner .series-band { background: var(--yellow-soft); }
  .label--veltliner .variety-band { background: var(--yellow); }

  .label--sparkling { background: var(--night); }
  .label--sparkling .brand-mark { border-color: var(--gold); }
  .label--sparkling .brand-name,
  .label--sparkling .brand-tagline { color: var(--silver); }
  .sparkling-title {
    margin-top: 26px;
    font-family: "Allura", cursive; font-size: 28px; color: var(--silver);
  }
</style>
</head>
<body>
<main class="label-row">
  <section class="label label--blaufrankisch">
    <div class="brand-mark"></div>
    <div class="brand-name">HALDEN</div>
    <div class="brand-tagline">WINE SINCE 1951</div>
    <div class="series-band">[SOLSTICE]</div>
    <div class="variety-band">BLAUFRANKISCH</div>
  </section>
  <section class="label label--pinot">
    <div class="brand-mark"></div>
    <div class="brand-name">HALDEN</div>
    <div class="brand-tagline">WINE SINCE 1951</div>
    <div class="series-band">[SOLSTICE]</div>
    <div class="variety-band">PINOT BLANC</div>
  </section>
  <section class="label label--cabernet">
    <div class="brand-mark"></div>
    <div class="brand-name">HALDEN</div>
    <div class="brand-tagline">WINE SINCE 1951</div>
    <div class="series-band">[SOLSTICE]</div>
    <div class="variety-band">CABERNET</div>
  </section>
  <section class="label label--veltliner">
    <div class="brand-mark"></div>
    <div class="brand-name">HALDEN</div>
    <div class="brand-tagline">WINE SINCE 1951</div>
    <div class="series-band">[SOLSTICE]</div>
    <div class="variety-band">GRUNER VELTLINER</div>
  </section>
  <section class="label label--sparkling">
    <div class="brand-mark"></div>
    <div class="brand-name">HALDEN</div>
    <div class="brand-tagline">WINE SINCE 1951</div>
    <div class="sparkling-title">Sparkling Wine</div>
  </section>
</main>
</body>
</html>
```